International Financial Organization needs a new Digital Workplace home page design

We need creative designs for the new Digital Workplace that will replace the current Intranet for an international organization based in Washington DC.

Organization Background: An organization of 189 countries, working to foster global monetary cooperation, secure financial stability, facilitate international trade, promote high employment and sustainable economic growth, and reduce poverty around the world.

Digital Workplace: The Digital workplace will be the central location that allows employees to do their work in productive, simple, and integrated manner.
Knowledge and Information are the lifeblood of our organization. Economists and experts conduct a lot of data-heavy research and produce a lot of reports and documents. The digital workplace will need to facilitate sharing of knowledge and collaboration among employees, and save them the hassle from going to multiple digital locations to do their work. Therefore the seamless integration of systems, and mobile-first design, is key.

Country Missions: A number of our economists travel on "missions" to countries all over the world on periodic basis to meet with country officials, present and discuss findings, and provide consultation. Before they go on missions, these economist do a lot of preparation and research about that country, and they collaborate in teams. When on mission (sometimes in areas that have very limited bandwidth connectivity) they need access to their documents, research, and resources and they need to collaborate with one another. Therefore mobility (zelkorm, tavlo, laptop and desktops) and personalization are very important design criteria. When they are back from their mission they need to document reports and findings, and they will need to work on that through multiple systems.

Design Concept: We attach a concept of the digital workplace homepage (power point slides). The concept offers three views (the three tabs at the top: Enterprise View, Departmental View, and My View.)
The enterprise view is meant to be for all the users in the organization, and displays information that the org want to push to all employees. Not much of personalization is listed in this this view. We only provide the name of potential tiles there. Please be creative and think out of the box, we are open for ideas. The second view is the departmental view. It is meant to focus on the news, events, and information that the department want to share with me as an employee of that department. We only provide the name of potential tiles there. Please be creative and think out of the box, we are open for ideas.
Finally, “My View” is illustrated with sample tiles of what we envision to be used there. We provide two variations for our vision of the “My View”. The tiles that are listed there are not meant to be in that same exact location. Please feel free to change the groupings of these tiles as the page allows (We had to fit our design on 16:9 PPT slide so it’s a not a real page). Also, these tiles are not mean to be restrictive, please be creative and suggest other tiles as you’d envision a modern Digital Workplace. We are open for ideas!

Deliverables: we expect to see at least one creative design per each of these 3 views of the home page for desktop view, and the equivalent in mobile view. In addition we expect any other views/variations that your creativity inspires.

Preferred color pallet: blue, green, orange, and all their gradients. Also open for other colors as your creativity inspires for an established, very mature, and well-respected, international financial organization.

Thank you!

```html
<!DOCTYPE html>
<html lang="en">
<head>
<meta charset="utf-8">
<title>WorkHub – My Work</title>
<link href="https://fonts.googleapis.com/css2?family=Montserrat:wght@400;500;600;700&display=swap" rel="stylesheet">
<style>
:root{
  --blue-top:#2f93d3;
  --blue-bottom:#2b70b0;
  --orange:#f47b20;
  --ink:#2b2b2b;
  --muted:#8a8a8a;
  --faint:#b9b9b9;
  --line:#e6e6e6;
  --row:#f6f6f6;
  --page:#f2f2f2;
  --card:#ffffff;
  --side-text:rgba(255,255,255,.55);
  --green:#3cc23c;
  --navy:#2a3f9a;
}
*{box-sizing:border-box;margin:0;padding:0}
html,body{width:1200px;height:1002px;overflow:hidden}
body{font-family:'Montserrat',sans-serif;color:var(--ink);background:var(--page);position:relative}
.topbar{position:absolute;left:0;top:0;width:1200px;height:53px;background:#fff;box-shadow:0 1px 4px rgba(0,0,0,.08);z-index:2}
.brand{position:absolute;left:15px;top:13px;font-size:21px;font-weight:600;color:#333}
.menu-toggle{position:absolute;left:161px;top:21px}
.global-nav{position:absolute;left:210px;top:20px;font-size:10.5px;display:flex;gap:29px;color:#333}
.global-nav b{font-weight:600;margin-right:-11px}
.user-chip{position:absolute;left:1027px;top:11px;display:flex;gap:10px;align-items:center}
.avatar{border-radius:50%;background:radial-gradient(circle at 50% 40%,#9aa3ad,#4c5560)}
.user-chip .name{font-size:11px;color:#333}
.user-chip .status{font-size:7.5px;color:var(--orange);font-weight:500;margin-top:3px}

.sidebar{position:absolute;left:0;top:53px;width:187px;height:949px;background:linear-gradient(180deg,var(--blue-top),var(--blue-bottom))}
.side-profile{position:absolute;left:14px;top:23px;display:flex;gap:10px;align-items:center;color:#fff}
.side-profile .name{font-size:11px}
.side-profile .status{font-size:7.5px;font-weight:600;margin-top:4px;display:flex;align-items:center;gap:5px}
.side-profile .status i{width:7px;height:7px;border-radius:50%;background:#fff;display:inline-block}
.side-item{position:absolute;left:0;width:187px;height:29px;display:flex;align-items:center;gap:10px;padding-left:14px;font-size:8.5px;letter-spacing:.3px;color:var(--side-text);font-weight:500}
.side-item svg{width:14px;height:14px;stroke:currentColor;fill:none;stroke-width:1.3}
.side-item.active{background:var(--orange);color:#fff;top:71px}
.side-heading{position:absolute;left:15px;top:192px;font-size:8.5px;font-weight:600;color:#fff}

.page-title{position:absolute;left:210px;top:66px;font-size:23px;font-weight:600;color:#333}
.page-sub{position:absolute;left:210px;top:95px;font-size:10.5px;color:#333}

.card{position:absolute;background:var(--card);border:1px solid var(--line);box-shadow:0 1px 3px rgba(0,0,0,.04)}
.card-title{position:absolute;left:21px;top:21px;font-size:10.5px;font-weight:600;color:#333}
.see-all{position:absolute;right:12px;top:21px;font-size:10.5px;font-weight:600;color:var(--orange)}
.list{position:absolute;left:0;right:0;top:45px}
.row{height:45px;display:flex;align-items:center;padding-left:21px;gap:9px}
.row.alt{background:var(--row)}
.row .t{font-size:10.5px;color:#333}
.row .d{font-size:7.5px;color:#444;margin-top:2px}
.file-icon{width:17px;height:21px}

.email{height:45px;padding:4px 0 0 21px;font-size:10.5px;line-height:11px;color:#333}
.email b{font-weight:600;display:block}
.email .time{font-size:7px;color:#555;margin-top:2px}
.email.alt{background:var(--row)}

.meeting{position:absolute;left:22px;display:flex;align-items:center}
.sq{width:28px;height:28px;background:linear-gradient(135deg,#8b6a5a,#3b2e2a)}
.meeting .n{position:absolute;left:39px;font-size:10.5px;font-weight:600;width:80px}
.meeting .loc{position:absolute;left:113px;top:5px;font-size:10.5px;width:90px;line-height:12px}
.meeting .loc span{display:block;font-size:7.5px;color:#555}

.task{height:45px;padding:6px 0 0 23px}
.task .t{font-size:10.5px;color:#333}
.task .d{font-size:7.5px;color:#444;margin-top:3px}
.task.alt{background:var(--row)}

.convo{position:absolute;left:15px;display:flex;gap:10px}
.convo .avatar{width:30px;height:30px;flex:none}
.convo .who{font-size:9px;color:#333}
.convo .msg{font-size:9px;color:var(--muted);margin-top:4px;line-height:13.5px;width:150px}
.convo .ago{font-size:7px;color:var(--faint);margin-top:4px;display:flex;align-items:center;gap:5px;letter-spacing:.3px}
.convo .ago i{width:8px;height:8px;border:1px solid var(--faint);border-radius:50%;display:inline-block}
.thread-line{position:absolute;left:30px;width:1px;background:#ddd}
.reply-box{position:absolute;left:15px;width:241px;height:68px;border:1px solid #ddd;background:#fff}
.post-btn{position:absolute;left:204px;width:52px;height:22px;border-radius:4px;background:var(--orange);color:#fff;font-size:7.5px;font-weight:600;display:flex;align-items:center;justify-content:center}

.team{position:absolute;left:22px;display:flex;align-items:center}
.team .sq{width:30px;height:30px;background:linear-gradient(135deg,#c9b3a5,#6d5a52)}
.team .n{position:absolute;left:39px;font-size:10.5px;font-weight:600;white-space:nowrap}
.team .when{position:absolute;left:113px;top:3px;font-size:10.5px;width:80px;line-height:13px}
.team .when span{display:block;font-size:7.5px;color:#555}

.contacts{position:absolute;left:22px;top:51px;width:170px;height:400px;overflow:hidden}
.contact{height:41px;display:flex;align-items:center;gap:10px}
.contact .avatar{width:29px;height:29px;flex:none;background:radial-gradient(circle at 50% 40%,#c49a82,#5d4032)}
.contact .n{font-size:10.5px;font-weight:600;line-height:12px}
.contact .r{font-size:9px;font-weight:400;color:#333}
.contact.fade{opacity:.35}
.scroll-track{position:absolute;left:201px;top:51px;width:3px;height:350px;background:#eee}
.scroll-thumb{position:absolute;left:201px;top:51px;width:3px;height:261px;background:#c8c8c8}

.news-img{position:absolute;left:22px;width:126px;height:99px}
.news-city{top:51px;background:linear-gradient(180deg,#1b1f28,#3a3a3c 60%,#6b5a3a)}
.news-stone{top:166px;background:linear-gradient(135deg,#a99a6a,#6f6440 70%,#4b432c)}
.news-text{position:absolute;left:164px;width:230px}
.news-text h3{font-size:10.5px;font-weight:600;line-height:11.5px}
.news-text p{font-size:7.5px;color:#444;margin-top:6px;word-spacing:8px}

.chart{position:absolute;left:0;top:0}
.legend{position:absolute;left:36px;top:49px;font-size:9px;display:flex;align-items:center;gap:5px}
.legend i{width:8px;height:8px;border-radius:50%;background:var(--orange);display:inline-block}
.stat{position:absolute;top:228px}
.stat .lab{font-size:7px;color:var(--faint);letter-spacing:.3px}
.stat .val{font-size:17px;font-weight:600;color:#333;margin-top:4px}
.stat .trend{display:flex;align-items:center;gap:5px;font-size:8px;font-weight:600;margin-top:4px}
</style>
</head>
<body>

<header class="topbar">
  <div class="brand">WorkHub</div>
  <svg class="menu-toggle" width="12" height="10" viewBox="0 0 12 10"><path d="M0 1h12M0 5h12M0 9h12" stroke="#333" stroke-width="1.4"/></svg>
  <nav class="global-nav"><b>Global Nav:</b><span>Link 1</span><span>Link 2</span><span>Link 3</span></nav>
  <div class="user-chip">
    <div class="avatar" role="img" aria-label="Profile photo of Jane" style="width:30px;height:30px"></div>
    <div><div class="name">Good Morning Jane!</div><div class="status">ONLINE</div></div>
  </div>
</header>

<aside class="sidebar">
  <div class="side-profile">
    <div class="avatar" role="img" aria-label="Profile photo of Jane" style="width:30px;height:30px"></div>
    <div><div class="name">Good Morning Jane!</div><div class="status"><i></i>ONLINE</div></div>
  </div>
  <div class="side-item active"><svg viewBox="0 0 14 14"><path d="M1 1v12h12M3 10l3-4 3 2 4-5"/></svg>ENTERPRISE HOMEPAGE</div>
  <div class="side-item" style="top:101px"><svg viewBox="0 0 14 14"><rect x="2" y="2" width="10" height="10"/><path d="M4 5h6M4 7h6M4 9h6"/></svg>DEPT. VIEW</div>
  <div class="side-item" style="top:131px"><svg viewBox="0 0 14 14"><rect x="3" y="1" width="8" height="12" rx="1"/><path d="M6 11h2"/></svg>MY VIEW</div>
  <div class="side-heading">MY NAVIGATION:</div>
  <div class="side-item" style="top:212px"><svg viewBox="0 0 14 14"><path d="M2 3h10v7H6l-3 2v-2H2z"/></svg>CREATE NEW DOCUMENT</div>
  <div class="side-item" style="top:242px"><svg viewBox="0 0 14 14"><circle cx="7" cy="7" r="2"/><circle cx="7" cy="7" r="5"/></svg>CREATE NEW SPREADSHEET</div>
  <div class="side-item" style="top:272px"><svg viewBox="0 0 14 14"><circle cx="7" cy="4.5" r="2.5"/><path d="M2 13c0-3 2.5-5 5-5s5 2 5 5"/></svg>CREATE NEW EMAIL MESSAGE</div>
  <div class="side-item" style="top:302px"><svg viewBox="0 0 14 14"><path d="M2 3h10v7H6l-3 2v-2H2z"/></svg>SCHEDULE A MEETING</div>
  <div class="side-item" style="top:333px"><svg viewBox="0 0 14 14"><circle cx="7" cy="7" r="2"/><circle cx="7" cy="7" r="5"/></svg>CREATE NEW TASK</div>
  <div class="side-item" style="top:362px"><svg viewBox="0 0 14 14"><circle cx="7" cy="4.5" r="2.5"/><path d="M2 13c0-3 2.5-5 5-5s5 2 5 5"/></svg>BOOK TRAVEL</div>
  <div class="side-item" style="top:392px"><svg viewBox="0 0 14 14"><circle cx="7" cy="4.5" r="2.5"/><path d="M2 13c0-3 2.5-5 5-5s5 2 5 5"/></svg>SUBMIT EXPENSES</div>
</aside>

<h1 class="page-title">My Work</h1>
<p class="page-sub">Lorem Ipsum is simply dummy text of the printing and typesetting industry</p>

<section class="card" style="left:210px;top:125px;width:224px;height:187px">
  <h2 class="card-title">My Recent Docs</h2>
  <div class="list">
    <div class="row"><svg class="file-icon" viewBox="0 0 17 21"><path d="M1 1h10l5 5v14H1z M11 1v5h5" fill="none" stroke="#f47b20"/><path d="M4 10h9M4 13h9M4 16h9" stroke="#f47b20"/></svg><div><div class="t">Document file name 1</div><div class="d">20/12/2017</div></div></div>
    <div class="row alt"><svg class="file-icon" viewBox="0 0 17 21"><path d="M1 1h10l5 5v14H1z M11 1v5h5" fill="none" stroke="#f47b20"/><path d="M4 9l9 8M13 9l-9 8" stroke="#f47b20"/></svg><div><div class="t">Spreadsheet file name 2</div><div class="d">20/12/2017</div></div></div>
    <div class="row"><svg class="file-icon" viewBox="0 0 17 21"><path d="M1 1h10l5 5v14H1z M11 1v5h5" fill="none" stroke="#f47b20"/><path d="M4 14h9v4H4z" fill="none" stroke="#f47b20"/></svg><div><div class="t">PDF document file 3</div><div class="d">20/12/2017</div></div></div>
  </div>
</section>

<section class="card" style="left:458px;top:125px;width:224px;height:187px">
  <h2 class="card-title">My Recent Emails</h2>
  <div class="list" style="top:44px">
    <div class="email alt"><b>Peter Hollis</b>Lorem ipsum dolor sit amet...<div class="time">9:23 am</div></div>
    <div class="email"><b>Clara Penn</b>Et donec ligula feugiat<div class="time">9:23 am</div></div>
    <div class="email"><b>Owen Harlow</b>Dapibus imperdiet vitae co...<div class="time">9:23 am</div></div>
  </div>
</section>

<section class="card" style="left:705px;top:125px;width:224px;height:187px">
  <h2 class="card-title">My Upcoming Meetings</h2>
  <div class="meeting" style="top:50px"><div class="sq" role="img" aria-label="Photo of meeting organiser"></div><div class="n">Meeting 1</div><div class="loc">HQ2 7B-073<span>2:30pm</span></div></div>
  <div class="meeting" style="top:91px"><div class="sq" role="img" aria-label="Photo of meeting organiser"></div><div class="n">Meeting 2</div><div class="loc">HQ2 7B-073<span>2:30pm</span></div></div>
  <div class="meeting" style="top:132px"><div class="sq" role="img" aria-label="Photo of meeting organiser"></div><div class="n">Meeting 3</div><div class="loc">HQ2 7B-073<span>2:30pm</span></div></div>
</section>

<section class="card" style="left:953px;top:125px;width:224px;height:187px">
  <h2 class="card-title">My Tasks</h2><span class="see-all">See All</span>
  <div class="list" style="top:45px">
    <div class="task"><div class="t">Review Georgia's 2017 Article</div><div class="d">20/12/2017</div></div>
    <div class="task alt"><div class="t">Submit Conference Selections</div><div class="d">20/12/2017</div></div>
    <div class="task"><div class="t">Complete FSRV chapter 2 data</div><div class="d">20/12/2017</div></div>
  </div>
</section>

<section class="card" style="left:210px;top:338px;width:269px;height:622px">
  <h2 class="card-title">My Recent Conversations</h2>
  <div class="thread-line" style="top:83px;height:140px"></div>
  <div class="convo" style="top:55px"><div class="avatar" role="img" aria-label="Photo of Marcel Duvane"></div><div><div class="who">Marcel Duvane</div><div class="msg">Hello.</div><div class="ago"><i></i>1 MIN AGO</div></div></div>
  <div class="convo" style="top:115px"><div class="avatar" role="img" aria-label="Photo of Marcel Duvane"></div><div><div class="who">Marcel Duvane</div><div class="msg">How are you?</div><div class="ago"><i></i>1 SEC AGO</div></div></div>
  <div class="convo" style="top:183px"><div class="avatar" role="img" aria-label="Photo of Marcel Duvane"></div><div><div class="who">Marcel Duvane</div><div class="msg" style="margin-top:9px">Lorem ipsum dolor sit amet, consectetur adipiscing elit, se deiusmod tempor incididunt ut labore et dolore magna aliqua.»</div><div class="ago"><i></i>1 SEC AGO</div></div></div>
  <div class="reply-box" style="top:283px"></div>
  <div class="post-btn" style="top:358px">POST</div>
  <div class="convo" style="top:390px"><div class="avatar" role="img" aria-label="Photo of Marcel Duvane"></div><div><div class="who">Marcel Duvane</div><div class="msg">Lorem ipsum dolor .</div><div class="ago"><i></i>1 MIN AGO</div></div></div>
  <div class="convo" style="top:450px"><div class="avatar" role="img" aria-label="Photo of Marcel Duvane"></div><div><div class="who">Marcel Duvane</div><div class="msg">Lorem ipsum dolor sit amet.</div><div class="ago"><i></i>1 SEC AGO</div></div></div>
  <div class="reply-box" style="top:506px"></div>
  <div class="post-btn" style="top:582px">POST</div>
</section>

<section class="card" style="left:502px;top:338px;width:224px;height:187px">
  <h2 class="card-title">My Teams/Communities</h2><span class="see-all">See All</span>
  <div class="team" style="top:50px"><div class="sq" role="img" aria-label="Team photo"></div><div class="n">Bulgaria</div><div class="when">June 2017<span>Mission</span></div></div>
  <div class="team" style="top:91px"><div class="sq" role="img" aria-label="Team photo"></div><div class="n">Romania</div><div class="when">April 2017<span>Mission</span></div></div>
  <div class="team" style="top:132px"><div class="sq" role="img" aria-label="Team photo"></div><div class="n">Bulgaria Country Team</div></div>
</section>

<section class="card" style="left:502px;top:551px;width:224px;height:409px">
  <h2 class="card-title">My Colleagues / Frequent Contacts</h2>
  <div class="contacts">
    <div class="contact"><div class="avatar" role="img" aria-label="Colleague photo"></div><div class="n">Peter Hollis,<div class="r">Mission Chief</div></div></div>
    <div class="contact"><div class="avatar" role="img" aria-label="Colleague photo"></div><div class="n">Wen Lo,<div class="r">Senior Economist</div></div></div>
    <div class="contact"><div class="avatar" role="img" aria-label="Colleague photo"></div><div class="n">Senior Economist,<div class="r">Resident Rep</div></div></div>
    <div class="contact"><div class="avatar" role="img" aria-label="Colleague photo"></div><div class="n">Peter Hollis,<div class="r">Mission Chief</div></div></div>
    <div class="contact"><div class="avatar" role="img" aria-label="Colleague photo"></div><div class="n">Wen Lo,<div class="r">Senior Economist</div></div></div>
    <div class="contact"><div class="avatar" role="img" aria-label="Colleague photo"></div><div class="n">Senior Economist,<div class="r">Resident Rep</div></div></div>
    <div class="contact"><div class="avatar" role="img" aria-label="Colleague photo"></div><div class="n">Peter Hollis,<div class="r">Mission Chief</div></div></div>
    <div class="contact"><div class="avatar" role="img" aria-label="Colleague photo"></div><div class="n">Wen Lo,<div class="r">Senior Economist</div></div></div>
    <div class="contact fade"><div class="avatar" role="img" aria-label="Colleague photo"></div><div class="n">Senior Economist,<div class="r">Resident Rep</div></div></div>
  </div>
  <div class="scroll-track"></div><div class="scroll-thumb"></div>
</section>

<section class="card" style="left:750px;top:338px;width:426px;height:303px">
  <h2 class="card-title">My News Report</h2><span class="see-all">See All</span>
  <div class="news-img news-city" role="img" aria-label="Night skyline of a financial district"></div>
  <div class="news-text" style="top:65px"><h3>Banks' Preparations for Brexit Need to Improve - Central Banks (Northwire)</h3><p>9:45am 14/June/2017</p></div>
  <div class="news-img news-stone" role="img" aria-label="Weathered stone statue"></div>
  <div class="news-text" style="top:180px"><h3>Eurozone recovery broadening but gaps remain (Dispatch)</h3><p>9:45am 14/June/2017</p></div>
</section>

<section class="card" style="left:750px;top:669px;width:426px;height:291px">
  <h2 class="card-title">My Analytics</h2>
  <svg class="chart" width="426" height="291" viewBox="0 0 426 291">
    <defs><linearGradient id="area" x1="0" y1="0" x2="0" y2="1"><stop offset="0" stop-color="#f47b20" stop-opacity=".22"/><stop offset="1" stop-color="#f47b20" stop-opacity="0"/></linearGradient></defs>
    <line x1="0" y1="36" x2="426" y2="36" stroke="#e6e6e6"/>
    <g stroke="#ececec">
      <path d="M38 88H410M38 118H410M38 148H410M38 178H410"/>
      <path d="M38 74V178M110 74V178M186 74V178M261 74V178M335 74V178M410 74V178"/>
    </g>
    <g font-family="Montserrat,sans-serif" font-size="8" fill="#b5b5b5">
      <text x="15" y="91">150</text><text x="15" y="121">100</text><text x="19" y="151">50</text><text x="23" y="181">0</text>
      <text x="35" y="193">Sep 2015</text><text x="110" y="193">Oct 2015</text><text x="185" y="193">Nov 2015</text><text x="260" y="193">Dec 2015</text><text x="335" y="193">Jan 2016</text>
    </g>
    <path d="M38 165C60 125 85 105 110 111S160 140 186 142S235 127 261 127S305 146 335 148S385 160 410 164V178H38Z" fill="url(#area)"/>
    <path d="M38 165C60 125 85 105 110 111S160 140 186 142S235 127 261 127S305 146 335 148S385 160 410 164" fill="none" stroke="#f47b20" stroke-width="2.5"/>
    <line x1="261" y1="110" x2="261" y2="178" stroke="#ddd"/>
    <circle cx="261" cy="127" r="4" fill="#fff" stroke="#f47b20" stroke-width="2"/>
    <rect x="235" y="87" width="53" height="28" rx="2" fill="#4a4a4a"/>
    <path d="M257 115l4 4 4-4z" fill="#4a4a4a"/>
    <text x="261.5" y="99" text-anchor="middle" font-family="Montserrat,sans-serif" font-size="8" fill="#fff">London</text>
    <text x="261.5" y="110" text-anchor="middle" font-family="Montserrat,sans-serif" font-size="8" font-weight="600" fill="#fff">89,012</text>
    <line x1="0" y1="209" x2="426" y2="209" stroke="#e6e6e6"/>
  </svg>
  <div class="legend"><i></i>Search</div>
  <div class="stat" style="left:46px"><div class="lab">REGISTRATIONS</div><div class="val">+73%</div><div class="trend" style="color:var(--orange)"><svg width="22" height="10" viewBox="0 0 22 10"><path d="M0 8l3-5 3 4 3-6 3 5 3-3 3 4 4-2" fill="none" stroke="#f47b20"/><path d="M0 9.5h22" stroke="#f47b20"/></svg>5 ▲</div></div>
  <div class="stat" style="left:190px"><div class="lab">VIEWS</div><div class="val">42</div><div class="trend" style="color:var(--navy)"><svg width="22" height="10" viewBox="0 0 22 10"><path d="M0 8l3-5 3 4 3-6 3 5 3-3 3 4 4-2" fill="none" stroke="#2a3f9a"/><path d="M0 9.5h22" stroke="#2a3f9a"/></svg>5% ▼</div></div>
  <div class="stat" style="left:317px"><div class="lab">REGISTRATIONS</div><div class="val">1,234</div><div class="trend" style="color:var(--green)"><svg width="22" height="10" viewBox="0 0 22 10"><path d="M0 8l3-5 3 4 3-6 3 5 3-3 3 4 4-2" fill="none" stroke="#3cc23c"/><path d="M0 9.5h22" stroke="#3cc23c"/></svg>9% ▲</div></div>
</section>

</body>
</html>
```